Flyer design for retail store owners

i would need to have a flyer design for my retail shop customers to show that I am a mailbox store that has all major shipping vendors to for their shipping needs. Ensuring that they can take advantage of opening a house account at the store and billed monthly, word document has all the details. Please use stock images for the notary public, passport photos, mailbox brass pictures of my actual mailboxes are listed in the pictures. I need to make it POP and WOW these retail store owners as I am using it to advertise the business

```html
<!DOCTYPE html>
<html lang="en">
<head>
<meta charset="utf-8">
<title>Brisk Box &amp; Ship – Retail Owner Flyer</title>
<link rel="stylesheet" href="https://fonts.googleapis.com/css2?family=Inter:ital,wght@0,400;0,600;0,700;0,800;1,400&display=swap">
<style>
  :root{
    --stage:#d9d9d9;
    --red:#e2001a;
    --orange:#f7b035;
    --orange-deep:#f39a1e;
    --blue:#1f56d8;
    --blue-light:#3a7cf0;
    --ink:#111111;
    --paper:#ffffff;
    --paper-fade:#ececec;
    --frame:#f6b21a;
  }
  *{box-sizing:border-box;margin:0;padding:0}
  html,body{width:1200px;height:900px;overflow:hidden}
  body{background:var(--stage);font-family:"Inter",Arial,sans-serif;color:var(--ink);position:relative}

  .flyer{position:absolute;left:292px;top:20px;width:616px;height:860px;background:var(--paper);overflow:hidden;box-shadow:0 2px 8px rgba(0,0,0,.12)}
  .flyer-waves{position:absolute;inset:0}

  .brand-band{position:absolute;left:0;top:0;width:300px;height:118px}
  .brand-name{position:absolute;left:28px;top:30px;color:var(--paper);font-weight:700;font-size:31px;line-height:31px;letter-spacing:-.3px}

  .intro{position:absolute;left:24px;top:122px;width:240px;font-style:italic;font-size:12.6px;line-height:16.6px}

  .photo{position:absolute}
  .photo-mailboxes{left:263px;top:41px;width:326px;height:392px;background:linear-gradient(135deg,#e8b07a 0%,#d9995f 55%,#c9874d 100%);border-radius:2px}
  .photo-circle{border-radius:50%;border:7px solid var(--paper);}
  .photo-notary{left:215px;top:371px;width:166px;height:166px;background:radial-gradient(circle at 40% 45%,#f1eee9 0%,#cfc7bd 60%,#6d5e54 100%)}
  .photo-passport{left:376px;top:297px;width:170px;height:170px;background:radial-gradient(circle at 55% 50%,#25324d 0%,#1b2438 45%,#e9e9ec 75%)}

  .offer-box{position:absolute;left:22px;top:495px;width:211px;height:322px;background:var(--paper);border:3px solid var(--frame);border-radius:20px;padding:24px 12px 0 14px}
  .offer-price{color:var(--red);font-weight:600;line-height:1}
  .offer-price .amount{font-size:42px}
  .offer-price .unit{font-size:21px;margin-left:4px}
  .offer-term{font-weight:700;font-size:14.6px;margin-top:6px}
  .offer-list{list-style:none;margin-top:16px}
  .offer-list li{display:flex;align-items:center;gap:4px;font-size:11.4px;height:19.5px}
  .offer-list svg{width:16px;height:16px;flex:none}
  .promo{text-align:center;margin-top:14px;font-size:10.8px;line-height:14px}
  .promo strong{display:block;font-size:13px;font-weight:600;margin-bottom:1px}

  .deals{position:absolute;left:248px;top:566px;width:320px}
  .deals-title{color:var(--red);font-weight:700;font-size:17.5px;margin-left:20px;margin-bottom:14px}
  .deals p{font-size:11.3px;line-height:14.5px;margin-bottom:14px}
  .accent{color:var(--red);font-weight:600}

  .closing{position:absolute;left:288px;top:812px;display:flex;align-items:center;gap:14px}
  .closing-hook{color:var(--red);font-weight:700;font-size:22px}
  .closing-note{font-weight:600;font-size:11.3px;line-height:14px}
</style>
</head>
<body>
<main class="flyer">
  <svg class="flyer-waves" viewBox="0 0 616 860" width="616" height="860" aria-hidden="true">
    <defs>
      <linearGradient id="paperFade" x1="0" y1="0" x2="0" y2="1">
        <stop offset="0" stop-color="#ffffff"/>
        <stop offset="0.55" stop-color="#ffffff"/>
        <stop offset="1" stop-color="#ececec"/>
      </linearGradient>
      <linearGradient id="blueSweep" x1="0" y1="0" x2="1" y2="0">
        <stop offset="0" stop-color="#1f56d8"/>
        <stop offset="1" stop-color="#3a7cf0"/>
      </linearGradient>
    </defs>
    <rect x="0" y="0" width="616" height="440" fill="var(--orange)"/>
    <path d="M0,378 C110,372 180,400 250,470 C320,545 430,545 616,250 L616,500 C540,560 440,585 330,560 C250,540 190,430 0,430 Z" fill="url(#blueSweep)"/>
    <path d="M0,430 C190,430 250,540 330,560 C440,585 540,560 616,500 L616,860 L0,860 Z" fill="url(#paperFade)"/>
    <path d="M420,540 C500,530 570,500 616,440 L616,500 C560,545 490,560 420,548 Z" fill="var(--orange-deep)"/>
    <path d="M0,378 C40,376 70,380 85,388 L0,396 Z" fill="var(--blue)"/>
  </svg>

  <svg class="brand-band" viewBox="0 0 300 118" aria-hidden="true">
    <path d="M0,0 L298,0 C260,40 230,75 206,104 C198,114 190,118 178,118 L0,118 Z" fill="var(--red)"/>
  </svg>
  <h1 class="brand-name">Brisk Box<br>&amp; Ship</h1>

  <div class="photo photo-mailboxes" role="img" aria-label="Photo of a bank of brass-coloured rental mailboxes with one door open"></div>

  <p class="intro">Renting a mail box is one of the most efficient and cost saving methods for receiving your mail and packages. Instead of having to worry about private security, weather conditions, sorting, and deliveries; all you have to do is pick-up your mail from our secured facility each day except Sundays.&nbsp; You will get a notification when mail arrives whether envelope or package, it will be scanned in daily which other mailbox stores do not offer! We offer onsite Notary Public with no appointments and onsite Passport Photos and can ship out same day.</p>

  <div class="photo photo-circle photo-notary" role="img" aria-label="Photo of a fountain pen and a sealed document for notary services"></div>
  <div class="photo photo-circle photo-passport" role="img" aria-label="Photo of two passports for passport photo services"></div>

  <svg width="0" height="0" style="position:absolute" aria-hidden="true">
    <symbol id="tick-circle" viewBox="0 0 16 16">
      <circle cx="8" cy="8.5" r="6.3" fill="none" stroke="#111" stroke-width="1.5"/>
      <path d="M4.6,8.3 L7.4,11 L14.5,2.5" fill="none" stroke="#111" stroke-width="2" stroke-linecap="round" stroke-linejoin="round"/>
    </symbol>
  </svg>

  <section class="offer-box">
    <div class="offer-price"><span class="amount">$12</span><span class="unit">a month</span></div>
    <div class="offer-term">for 6-12 months leases!</div>
    <ul class="offer-list">
      <li><svg><use href="#tick-circle"/></svg>Get a mailbox in the shop</li>
      <li><svg><use href="#tick-circle"/></svg>a book of stamps(20 count)</li>
      <li><svg><use href="#tick-circle"/></svg>3 notarizations by appointment</li>
      <li><svg><use href="#tick-circle"/></svg>a book of stamps(20 count)</li>
      <li><svg><use href="#tick-circle"/></svg>100 copies of black and white</li>
      <li><svg><use href="#tick-circle"/></svg>and 100 copies of color</li>
    </ul>
    <p class="promo"><strong>Exclusive Promo Deal!</strong>offering for all Maplewood Commons shopping center owners/employees</p>
  </section>

  <section class="deals">
    <h2 class="deals-title">Check out these other deals!</h2>
    <p>As a retail owner, you know how important it is to keep your customers coming back - you will get <span class="accent">20% discount for printing services.</span></p>
    <p>We duplicate keys for <span class="accent">$2/each</span>, our regular price charge is $4/each. <span class="accent">Save up to 50%!</span></p>
    <p>Lamination is also discounted at <span class="accent">10% off.</span></p>
    <p><span class="accent">10% off retail supplies ...</span> must be minimum of 10$</p>
    <p>For house accounts -a <span class="accent">5% discount</span> will be deducted monthly of billing change to invoicing PLUS we're giving another <span class="accent">5% of the discount</span> if you upgrade and sign up for mailbox.</p>
  </section>

  <div class="closing">
    <span class="closing-hook">Great right?</span>
    <span class="closing-note">Take advantage of this<br>limited time offer now!</span>
  </div>
</main>
</body>
</html>
```